Service Menu refresh 2018 Update of menu pricing

We currently have service menus as attached. We will be updating our look via our homepage image, our service menu and our in-house beverage and treatment menu.
We are a natural and sustainable hair salon group and moving more towards head spa which consists of treatments, beauty, tanning as well as your traditional hair services. Our imagery needs to reflect our efforts in spa treatments in the hair and scalp area and use natural materials and colours reflecting sustainability.
Elvu is the brand we stock and promote.

Target Market(s)

Men or women interesting in personal maintenance with natural and organic products and using sustainable practises

Industry/Entity Type

Hair And Beauty

Font styles to use
Sans Serif
Other font styles liked:
• Arial or Helvetica

Colors
9acb3c
abd037
cadf82
ffffff

Requirements
Must have
• Name on the front cover, locations on back cover
Nice to have
• Prestige feel, reflect male and female clients
Should not have
• Bold artificial writing or any type of cartoon images.
• Same images as existing menu.

```html
<!DOCTYPE html>
<html lang="en">
<head>
<meta charset="utf-8">
<title>Leafline Hair Studios – Service Menu</title>
<link rel="stylesheet" href="https://fonts.googleapis.com/css2?family=Open+Sans:wght@400;600&display=swap">
<style>
:root{
  --page:#ececec;
  --green:#7cbd3f;
  --green-card:#79b843;
  --green-dark:#3f6b47;
  --green-rule:#cfe6b4;
  --paper:#f4f4f4;
  --ink:#2b2b2b;
  --ink-soft:#555;
  --white:#ffffff;
}
*{box-sizing:border-box;margin:0;padding:0}
html,body{width:1075px;height:1200px;overflow:hidden;background:var(--page)}
body{font-family:"Open Sans",Arial,Helvetica,sans-serif;color:var(--ink)}
.stage{position:absolute;left:0;top:0;width:1274px;height:1422px;transform:scale(0.84379);transform-origin:0 0}
.card{position:absolute;left:95px;width:1115px;height:605px;overflow:hidden}
.card--front{top:60px;background:var(--paper)}
.card--back{top:740px;background:var(--green-card);color:var(--white)}

/* front */
.front-art{position:absolute;left:0;top:0}
.brand{position:absolute;left:560px;top:38px;display:flex;align-items:center;gap:18px}
.brand__dot{width:62px;height:62px;border-radius:50%;background:var(--green)}
.brand__name{font-size:42px;font-weight:400;color:var(--ink);letter-spacing:-0.5px}
.locations{position:absolute;left:657px;top:128px;list-style:none}
.location{height:84.5px}
.location__name{display:flex;align-items:center;gap:8px;font-size:19px;color:var(--ink);line-height:26px}
.location__name svg{flex:none}
.location__line{font-size:15px;color:var(--ink-soft);line-height:21px}
.web-band{position:absolute;left:714px;top:548px;width:401px;height:44px;background:var(--green);border-radius:22px 0 0 22px;color:var(--white);font-size:19px;line-height:44px;padding-left:24px;letter-spacing:0.3px}

/* back */
.back-art{position:absolute;right:0;top:0;width:470px;height:605px}
.brand--light{left:38px;top:28px}
.brand--light .brand__dot{background:var(--white)}
.brand--light .brand__name{color:var(--white)}
.note{position:absolute;left:583px;top:33px;width:479px;height:78px;border:1.5px solid var(--white);padding:12px 12px;font-size:11.6px;line-height:15.5px}
.menu{position:absolute;width:472px}
.menu--left{left:33px}
.menu--right{left:583px}
.section__head{display:grid;grid-template-columns:310px 45px 45px 45px 45px;font-size:19px;line-height:26px;border-bottom:1.5px solid var(--green-rule);padding-bottom:4px;margin-bottom:7px}
.section__head span:not(:first-child){text-align:left;padding-left:5px}
.row{display:grid;grid-template-columns:310px 45px 45px 45px 45px;line-height:15.5px;font-size:12px}
.row--main{font-size:15px}
.row span:not(:first-child){font-size:12px}
.note-line{font-size:12px;line-height:15.5px}
</style>
</head>
<body>
<div class="stage">

  <section class="card card--front">
    <svg class="front-art" width="1115" height="605" viewBox="0 0 1115 605">
      <defs>
        <linearGradient id="hairTone" x1="0" y1="0" x2="1" y2="1">
          <stop offset="0" stop-color="#d9c4ac"/>
          <stop offset="0.45" stop-color="#b59b80"/>
          <stop offset="0.75" stop-color="#8a7663"/>
          <stop offset="1" stop-color="#c9b8a4"/>
        </linearGradient>
      </defs>
      <path d="M545 605 Q 620 300 525 0 L 560 0 Q 680 300 580 605 Z" fill="var(--green-dark)"/>
      <path d="M445 605 Q 590 300 480 0 L 525 0 Q 620 300 545 605 Z" fill="var(--green)"/>
      <path d="M440 605 Q 575 300 472 0 L 484 0 Q 590 300 452 605 Z" fill="var(--white)"/>
      <path role="img" aria-label="Photograph of a model in profile with long, glossy, flowing blonde hair" d="M0 0 L472 0 Q 575 300 440 605 L0 605 Z" fill="url(#hairTone)"/>
    </svg>

    <div class="brand">
      <span class="brand__dot"></span>
      <span class="brand__name">Leafline Hair Studios</span>
    </div>

    <ul class="locations">
      <li class="location">
        <div class="location__name"><svg width="12" height="17" viewBox="0 0 12 17"><path d="M6 0a6 6 0 0 1 6 6c0 4.5-6 11-6 11S0 10.5 0 6a6 6 0 0 1 6-6z" fill="var(--green)"/><circle cx="6" cy="6" r="2.2" fill="var(--paper)"/></svg>MARLOW PARK</div>
        <div class="location__line">Fern Road, Marlow Park Plaza, 4150</div>
        <div class="location__line">p: 07 5550 1201&nbsp;&nbsp;&nbsp; e: marlowpark@leaflinestudios.com.au</div>
      </li>
      <li class="location">
        <div class="location__name"><svg width="12" height="17" viewBox="0 0 12 17"><path d="M6 0a6 6 0 0 1 6 6c0 4.5-6 11-6 11S0 10.5 0 6a6 6 0 0 1 6-6z" fill="var(--green)"/><circle cx="6" cy="6" r="2.2" fill="var(--paper)"/></svg>KESTREL HILL</div>
        <div class="location__line">Wren Road, Kestrel Hill Centre, 4030</div>
        <div class="location__line">p: 07 5550 1202&nbsp;&nbsp;&nbsp; e: kestrelhill@leaflinestudios.com.au</div>
      </li>
      <li class="location">
        <div class="location__name"><svg width="12" height="17" viewBox="0 0 12 17"><path d="M6 0a6 6 0 0 1 6 6c0 4.5-6 11-6 11S0 10.5 0 6a6 6 0 0 1 6-6z" fill="var(--green)"/><circle cx="6" cy="6" r="2.2" fill="var(--paper)"/></svg>WILLOWBANK</div>
        <div class="location__line">Alder Road, Willowbank Shopping Village, 4066</div>
        <div class="location__line">p: 07 5550 1203&nbsp;&nbsp;&nbsp; e: willowbank@leaflinestudios.com.au</div>
      </li>
      <li class="location">
        <div class="location__name"><svg width="12" height="17" viewBox="0 0 12 17"><path d="M6 0a6 6 0 0 1 6 6c0 4.5-6 11-6 11S0 10.5 0 6a6 6 0 0 1 6-6z" fill="var(--green)"/><circle cx="6" cy="6" r="2.2" fill="var(--paper)"/></svg>CEDAR BAY</div>
        <div class="location__line">Harbour Street, Cedar Bay Centre, 4069</div>
        <div class="location__line">p: 07 5550 1204&nbsp;&nbsp;&nbsp; e: marlowpark@leaflinestudios.com.au</div>
      </li>
      <li class="location">
        <div class="location__name"><svg width="12" height="17" viewBox="0 0 12 17"><path d="M6 0a6 6 0 0 1 6 6c0 4.5-6 11-6 11S0 10.5 0 6a6 6 0 0 1 6-6z" fill="var(--green)"/><circle cx="6" cy="6" r="2.2" fill="var(--paper)"/></svg>HARBOURSIDE MEDICAL PRECINCT</div>
        <div class="location__line">Lantern St, Harbourside, 4028</div>
        <div class="location__line">p: 07 5550 1205&nbsp;&nbsp;&nbsp; e: harbourside@leaflinestudios.com.au</div>
      </li>
    </ul>

    <div class="web-band">WWW.LEAFLINESTUDIOS.COM.AU</div>
  </section>

  <section class="card card--back">
    <svg class="back-art" role="img" aria-label="Faint botanical illustration of tropical leaves and ferns" viewBox="0 0 470 605" preserveAspectRatio="none">
      <defs>
        <radialGradient id="foliage" cx="0.65" cy="0.45" r="0.75">
          <stop offset="0" stop-color="#6aa83a" stop-opacity="0.8"/>
          <stop offset="1" stop-color="#79b843" stop-opacity="0"/>
        </radialGradient>
      </defs>
      <rect width="470" height="605" fill="url(#foliage)"/>
    </svg>

    <div class="brand brand--light">
      <span class="brand__dot"></span>
      <span class="brand__name">Leafline Hair Studios</span>
    </div>

    <div class="note">*Pricing is indicative of average products used and time taken for each service.<br>You will always receive a firm price after your consultation.<br>S to the jaw line | M to the collarbone | L to the bra strap | Xl past bra strap</div>

    <div class="menu menu--left" style="top:143px">
      <div class="section__head"><span>CUT &amp; BLOW-DRY</span><span>S</span><span>M</span><span>L</span><span>XL</span></div>
      <div class="row row--main"><span>LADIES</span><span>$77</span><span>$88</span><span>$99</span><span>$110</span></div>
      <div class="row row--main"><span>FRINGE</span></div>
      <div class="row"><span>Trim</span><span>$25</span></div>
      <div class="row"><span>Restyle</span><span>$35</span></div>
      <div class="row row--main"><span>MENS</span></div>
      <div class="row"><span>Single blade clipper</span><span>$28</span></div>
      <div class="row"><span>Style cut</span><span>$42</span></div>
      <div class="row row--main"><span>CHILDREN</span></div>
      <div class="row"><span>10 and under</span><span>$24</span></div>
      <div class="row"><span>11-16 Male</span><span>$32</span></div>
      <div class="row"><span>11-16 Female</span><span>$48</span></div>
      <div class="row"><span>add a wash</span><span>$5</span></div>
      <div class="row row--main"><span>BLOWDRY</span><span>$47</span><span>$57</span><span>$67</span><span>$77</span></div>
      <div class="row"><span>Shampoo &amp; dry off</span><span>$25</span></div>
    </div>

    <div class="menu menu--left" style="top:413px">
      <div class="section__head"><span>TREATMENTS</span></div>
      <div class="row"><span>Deep treatment</span><span>$35</span></div>
      <div class="row"><span>Head.Spa ritual</span><span>$65</span></div>
    </div>

    <div class="menu menu--left" style="top:499px">
      <div class="section__head"><span>UPSTILE</span></div>
      <div class="row"><span>45 minutes</span><span>$85</span></div>
      <div class="row"><span>60 minutes</span><span>$120</span></div>
    </div>

    <div class="menu menu--right" style="top:143px">
      <div class="section__head"><span>COLOUR</span><span>S</span><span>M</span><span>L</span><span>XL</span></div>
      <div class="row row--main"><span>REGROWTH</span><span>$83</span></div>
      <div class="row row--main"><span>FULL COLOR TINT</span><span>$125</span><span>$145</span><span>$165</span><span>$185</span></div>
      <div class="row row--main"><span>REGROWTH&nbsp; LIGHTENTING</span><span>$165</span><span>$189</span><span>$209</span><span>$229</span></div>
      <div class="row row--main"><span>BALAYAGE/OMBRE</span><span></span><span>$275</span><span>$375</span><span>$475</span></div>
    </div>

    <div class="menu menu--right" style="top:257px">
      <div class="section__head"><span>VERDE TINT</span></div>
      <div class="row row--main"><span>REGROWTH</span><span>$99</span></div>
      <div class="row row--main"><span>FULL COLOR TINT</span><span>$155</span><span>$175</span><span>$195</span><span>$205</span></div>
    </div>

    <div class="menu menu--right" style="top:343px">
      <div class="section__head"><span>FOILS</span></div>
      <div class="row row--main"><span>SINGLE</span><span>$11</span><span>$13</span><span>$17</span><span>$22</span></div>
      <div class="row row--main"><span>1/4 HEAD</span><span>$135</span><span>$155</span><span>$175</span><span>$195</span></div>
      <div class="row row--main"><span>1/2 HEAD</span><span>$185</span><span>$205</span><span>$235</span><span>$265</span></div>
      <div class="row row--main"><span>FULL HEAD</span><span>$235</span><span>$265</span><span>$315</span><span>$355</span></div>
    </div>

    <div class="menu menu--right" style="top:459px">
      <div class="section__head"><span>STRAIGHT</span></div>
      <div class="row row--main"><span>KERATIN STRAIGHTENING SYSTEM</span><span>$365</span><span>$445</span><span>$535</span><span>$565</span></div>
      <div class="note-line">Including colour mach &amp; toner</div>
      <div class="note-line">Minimum 6 foils without colour</div>
      <div class="note-line">Minimum change on a Sunday is $40</div>
    </div>
  </section>

</div>
</body>
</html>
```